Pastry Trade Institute Website Homepage Revision

I need the "homepage" to the new Northfield Pastry Trade Institute to reworked. The current homepage is dull. It needs the attention of a professional graphic artist so it delivers a professionally finished feel and look. I have included the current URL for your viewing (builds.vorlimo.com/bridal-torte/cms/ ) to see where we are in the development phase. The elements on the homepage are all necessary and the colors are correct. I have also included the original Word document for the page (you can extract the RGB values and images from the doc). To be clear, I am not looking to recreate all the web pages, just the homepage. It needs to be responsive and stretched.

Target Market(s)

All bakers who sell wedding cakes in the United States

Number of Pages Required

1 page

Font styles to use
Other font styles liked:
• see the Word Document

Requirements
Must have
• It must have the elements already in the original mock up. That includes the colors and fonts.

```html
<!DOCTYPE html>
<html lang="en">
<head>
<meta charset="utf-8">
<title>Northfield Pastry Trade Institute – Homepage</title>
<link href="https://fonts.googleapis.com/css2?family=Lora:ital,wght@0,400;0,600;0,700;1,400;1,700&display=swap" rel="stylesheet">
<style>
:root{
  --pink:#e8336b;
  --teal:#00c2c4;
  --teal-dark:#0a4d4f;
  --yellow:#f7b500;
  --mist:#d3dfe0;
  --plum:#a3125e;
  --ink:#1b1b1b;
  --muted:#666;
  --white:#fff;
}
*{margin:0;padding:0;box-sizing:border-box}
html,body{width:1200px;height:1200px;overflow:hidden;background:#fff}
body{font-family:"Lora",Georgia,serif;color:var(--ink)}
.canvas{position:relative;width:1200px;height:1200px;overflow:hidden;background:#fff}
.page{position:absolute;left:437px;top:0;width:1020px;height:3750px;transform:scale(.32);transform-origin:0 0;background:#fff;box-shadow:0 0 60px rgba(0,0,0,.12)}
.abs{position:absolute}
.btn{display:inline-flex;align-items:center;justify-content:center;border-radius:40px;font-weight:700;font-family:"Lora",Georgia,serif}

/* header + hero */
.brand{left:148px;top:22px;width:160px;text-align:center;color:var(--pink);font-size:17px;font-style:italic}
.brand .dot{display:block;width:26px;height:26px;border-radius:50%;border:3px solid var(--pink);margin:0 auto 8px}
.menu-dot{left:740px;top:28px;width:30px;height:30px;border-radius:50%;border:2px solid var(--pink)}
.login{left:785px;top:28px;width:88px;height:30px;border:2px solid var(--pink);color:var(--pink);font-size:11px}
.hero-title{left:148px;top:108px;font-size:48px;line-height:56px;font-weight:400}
.hero-title b{font-weight:700;font-size:52px}
.hero-text{left:148px;top:240px;width:340px;font-size:12px;line-height:17px;color:#333}
.hero-btn{left:148px;top:320px;width:145px;height:36px;background:var(--pink);color:#fff;font-size:11px;gap:10px}
.cake{left:560px;top:70px;width:315px;height:325px;border-radius:40% 40% 20% 20%;background:radial-gradient(circle at 50% 40%,#f4ede6 0,#6b3b2a 55%,#c1253a 80%,#fff 100%)}
.seen-line{left:-120px;right:-120px;top:440px;height:1px;background:#e3e3e3}
.seen{left:128px;top:392px;width:745px;height:88px;background:#fff;border:1px solid #e6e6e6;border-radius:6px;display:flex;align-items:center;padding:0 22px;gap:30px}
.seen-label{font-size:14px;line-height:17px;color:#555;width:110px;border-right:1px solid #ddd}
.badge{width:40px;height:40px;background:#c9c9c9;border-radius:6px}
.badge.round{border-radius:50%;background:#9c9c9c}

/* video + optin */
.video{left:128px;top:520px;width:432px;height:370px;background:linear-gradient(135deg,#1e5a6e,#5fd0d0 55%,#b9ecec);border-radius:3px 0 0 3px}
.video-frame{position:absolute;left:42px;top:58px;width:352px;height:90px;border:5px solid #fff;display:flex;align-items:center;justify-content:center;color:#fff;font-size:30px;font-weight:700}
.video-btn{position:absolute;left:132px;top:185px;width:175px;height:52px;background:#fff;color:#111;font-size:20px}
.optin{left:560px;top:520px;width:313px;height:370px;border:5px solid var(--teal);background:#fff;text-align:center;padding:28px 20px}
.optin h3{font-size:21px;line-height:29px;font-weight:700}
.optin h3 span{font-weight:400}
.optin h3 em{font-style:normal;font-size:28px}
.field{display:block;height:34px;border:2px solid #333;border-radius:4px;font-size:11px;text-align:left;padding:9px 14px;margin:0 28px 18px}
.optin .field:first-of-type{margin-top:30px}
.watch{width:206px;height:48px;background:var(--yellow);font-size:17px;gap:12px;margin-top:6px}
.play{width:22px;height:22px;border-radius:50%;background:#111;display:inline-block;position:relative}
.play:after{content:"";position:absolute;left:8px;top:6px;border-left:8px solid #fff;border-top:5px solid transparent;border-bottom:5px solid transparent}

/* teal band */
.band{left:0;top:932px;width:1020px;height:443px;background:var(--teal);color:#fff;text-align:center}
.band .kicker{position:absolute;top:30px;width:100%;font-size:25px;opacity:.9}
.band .headline{position:absolute;top:68px;width:100%;font-size:31px;font-weight:700;letter-spacing:1px}
.path{position:absolute;top:150px;width:170px;text-align:center;margin-left:-85px}
.ring{width:88px;height:88px;border:3px solid #fff;border-radius:50%;margin:0 auto 28px;display:flex;align-items:center;justify-content:center}
.path p{font-size:19px;line-height:29px}
.path .link{margin-top:18px;font-size:12px;display:flex;align-items:center;justify-content:center;gap:10px;text-decoration:underline}
.path .link:before,.path .link:after{content:"";width:26px;height:1px;background:#fff}

/* cards */
.card{top:1420px;width:225px;height:505px;background:#fff;box-shadow:0 4px 14px rgba(0,0,0,.12);border-radius:4px;text-align:center}
.card .photo{height:210px;border-radius:4px 4px 0 0}
.card p{font-size:17px;line-height:29px;font-style:italic;padding:24px 18px 0;color:#333}
.card p b{font-style:normal;font-weight:700;color:#111}
.card .btn{position:absolute;left:40px;bottom:30px;width:145px;height:38px;background:var(--yellow);font-size:14px}

/* proof section */
.proof{left:0;top:1980px;width:1020px;height:765px;background:var(--mist)}
.proof h2{position:absolute;left:148px;top:38px;width:725px;font-size:32px;line-height:46px;font-weight:700;text-align:justify;text-align-last:center}
.portrait{position:absolute;left:148px;top:212px;width:222px;height:363px;background:linear-gradient(160deg,#ffffff,#f0d2b6 45%,#ffffff 70%,#2c2c2c);overflow:hidden}
.ribbon{position:absolute;right:-44px;top:28px;width:170px;height:34px;background:var(--pink);transform:rotate(45deg);color:#fff;font-size:14px;font-style:italic;display:flex;align-items:center;justify-content:center}
.proof .copy{position:absolute;left:423px;top:212px;width:450px;font-size:16px;line-height:28px;color:#555;text-align:justify}
.proof .copy p{margin-bottom:28px}
.enter{position:absolute;left:148px;top:592px;font-size:29px;font-style:italic}
.enter b{font-style:normal}
.advisory{position:absolute;left:182px;top:682px;width:695px;font-size:14px;line-height:28px;color:#222}
.arrow{position:absolute;left:118px;top:640px}

/* join */
.join{left:0;top:2745px;width:1020px;height:455px;background:var(--teal);color:#fff;text-align:center}
.join h2{position:absolute;top:35px;left:150px;width:720px;font-size:41px;line-height:58px;font-style:italic;font-weight:400}
.join h2 b{font-weight:700}
.join .lead{position:absolute;top:162px;left:148px;width:725px;font-size:19px;line-height:32px;font-style:italic;opacity:.92}
.join .lead b{font-style:normal;font-weight:700}
.joinbar{position:absolute;left:148px;top:295px;width:725px;height:92px;background:var(--teal-dark);border-radius:6px;display:flex;align-items:center;padding:0 28px;gap:24px}
.joinbar .in{width:208px;height:38px;border:2px solid var(--teal);font-size:13px;font-weight:700;text-align:left;padding:10px 12px}
.joinbar .btn{margin-left:8px;width:180px;height:50px;background:var(--yellow);color:#222;font-size:17px}
.join .note{position:absolute;top:420px;width:100%;font-size:10px;color:var(--teal-dark)}

/* footer */
.footer{left:0;top:3200px;width:1020px;height:550px;background:var(--plum);color:#fff}
.f-brand{position:absolute;left:165px;top:40px;width:150px;text-align:center;font-size:16px;font-style:italic}
.f-brand .dot{display:block;width:24px;height:24px;border:3px solid #fff;border-radius:50%;margin:0 auto 8px}
.socials{position:absolute;left:185px;top:122px;display:flex;gap:12px}
.socials span{width:28px;height:28px;border:2px solid #fff;border-radius:50%}
.blog{position:absolute;left:343px;top:40px;width:532px}
.blog h4{font-size:20px;margin-bottom:18px}
.post{display:flex;align-items:center;height:38px;font-size:13px;font-weight:700}
.post .date{width:68px;font-size:10px;font-weight:400;opacity:.8}
.post .rm{margin-left:auto;width:88px;height:22px;border:2px solid #fff;border-radius:20px;font-size:10px;font-weight:400}
.older{text-align:right;font-size:11px;text-decoration:underline;margin-top:4px}
.col{position:absolute;top:212px}
.col h5{font-size:17px;font-weight:700;margin-bottom:20px}
.col a{display:block;color:#fff;font-size:13px;line-height:27.5px;text-decoration:underline}
.copyright{position:absolute;left:152px;top:495px;font-size:12px}
</style>
</head>
<body>
<div class="canvas">
 <div class="page">

  <!-- header -->
  <div class="abs brand"><span class="dot"></span>Northfield Pastry</div>
  <div class="abs menu-dot"></div>
  <div class="abs btn login">Login</div>

  <!-- hero -->
  <h1 class="abs hero-title">Be the best in<br><b>Wedding Cakes</b></h1>
  <p class="abs hero-text">Take a tour with Us lorem ipsum dolor sit amet consectetur adip piscing dolor sit amet. If you are interested, contact Us anytime.</p>
  <div class="abs btn hero-btn">Discover more
   <svg width="14" height="12" viewBox="0 0 14 12"><path d="M1 6h11M7 1l5 5-5 5" stroke="#fff" stroke-width="2" fill="none"/></svg></div>
  <div class="abs cake" role="img" aria-label="Photo of a tiered wedding cake with chocolate drip and berries"></div>

  <div class="abs seen-line"></div>
  <div class="abs seen">
   <div class="seen-label">RAY DUNMORE AS SEEN ON</div>
   <span class="badge"></span><span class="badge"></span><span class="badge"></span>
   <span class="badge round"></span><span class="badge"></span><span class="badge"></span><span class="badge"></span>
  </div>

  <!-- video + optin -->
  <div class="abs video" role="img" aria-label="Video still of a baker decorating a cake">
   <div class="video-frame">Watch This First</div>
   <div class="btn video-btn">Click Here</div>
  </div>
  <div class="abs optin">
   <h3><em>How</em> <span>a New Discovery</span> Sells More Wedding Cakes and at Higher Prices!</h3>
   <span class="field">Your First Name</span>
   <span class="field">Your E-mail</span>
   <div class="btn watch">WATCH NOW! <span class="play"></span></div>
  </div>

  <!-- teal band -->
  <section class="abs band">
   <p class="kicker">Our research is not just a game changer. It is the game changer.</p>
   <p class="headline">WE'RE REWRITING THE BOOK FOR SELLING</p>
   <div class="path" style="left:223px">
    <div class="ring"><svg width="40" height="40" viewBox="0 0 40 40" fill="none" stroke="#fff" stroke-width="2"><path d="M20 5a10 10 0 0 0-6 18v6h12v-6a10 10 0 0 0-6-18zM15 33h10M17 37h6"/></svg></div>
    <p>I'm <b>NEW</b> to Selling Wedding Cakes</p><div class="link">Click Here</div>
   </div>
   <div class="path" style="left:415px">
    <div class="ring"><svg width="40" height="40" viewBox="0 0 40 40" fill="none" stroke="#fff" stroke-width="2"><path d="M8 32h24M10 32V22h20v10M13 22v-7h14v7M20 8v7"/></svg></div>
    <p>I Want to <b>MAINTAIN</b> my sales</p><div class="link">Click Here</div>
   </div>
   <div class="path" style="left:610px">
    <div class="ring"><svg width="40" height="40" viewBox="0 0 40 40" fill="none" stroke="#fff" stroke-width="2"><path d="M6 34h28M10 34V22h5v12M18 34V16h5v18M26 34V10h5v24"/></svg></div>
    <p>I'm Eager to <b>BOOST</b> My Sales and Profits</p><div class="link">Click Here</div>
   </div>
   <div class="path" style="left:803px">
    <div class="ring"><svg width="40" height="40" viewBox="0 0 40 40" fill="none" stroke="#fff" stroke-width="2"><path d="M20 5l4.5 9.5 10 1.2-7.4 7 2 10L20 28l-9.1 4.7 2-10-7.4-7 10-1.2z"/></svg></div>
    <p>I'm Ready to <b>DOMINATE</b> My Market Area</p><div class="link">Click Here</div>
   </div>
  </section>

  <!-- cards -->
  <article class="abs card" style="left:148px">
   <div class="photo" role="img" aria-label="Photo of smiling chefs holding a book" style="background:linear-gradient(180deg,#e9e9e9,#b23a3a)"></div>
   <p><b>Become</b> the "World's Greatest." You'll have an atmosphere so special, brides won't think of using anyone but you!</p>
   <div class="btn">More</div>
  </article>
  <article class="abs card" style="left:395px">
   <div class="photo" role="img" aria-label="Photo of a puzzled woman beside a question mark" style="background:linear-gradient(90deg,#2a2a2a,#6d6d6d)"></div>
   <p><b>Peek</b> at a very effective psychological sales riddle called "The Insecurity Gap."</p>
   <div class="btn">More</div>
  </article>
  <article class="abs card" style="left:645px">
   <div class="photo" role="img" aria-label="Photo of a split portrait in colour and grey" style="background:linear-gradient(90deg,#e8c79a,#d8d8d8)"></div>
   <p><b>Discover</b> a sales growth secret that reveals the "Two Faces of Your Wedding Cake Business."</p>
   <div class="btn">More</div>
  </article>

  <!-- proof -->
  <section class="abs proof">
   <h2>Use Cutting-edge Methods Proven to Get MORE Leads, Convince MORE Brides to Choose You, Get HIGHER Prices and DOMINATE Your Competition.</h2>
   <div class="portrait" role="img" aria-label="Portrait photo of the institute founder in chef's whites">
    <div class="ribbon">Ray Dunmore</div>
   </div>
   <div class="copy">
    <p>Our breakthrough marketing and sales methods are possible due to the long-term studies we've conducted with 150, 000 brides over the past 12 years.</p>
    <p>From the findings, we have developed new and revolutionary marketing strategies, sales tools, and a complete transformational wedding cake sales system.</p>
    <p>But, don't take my word for it...let me "prove" the value and impact they will have on your wedding cake business.</p>
   </div>
   <p class="enter"><b>Enter</b> Your Name and Email Address Below.</p>
   <svg class="arrow" width="50" height="100" viewBox="0 0 50 100" fill="none" stroke="#2bbcc0" stroke-width="2"><path d="M28 4C10 20 8 50 20 90M10 78l10 14 8-16"/></svg>
   <p class="advisory">Each month you'll receive our "<b>Advanced Wedding Cake Marketing Advisory</b>." It's normally available for a $397 subscription fee. You'll receive the first year... <b>Absolutely FREE.</b></p>
  </section>

  <!-- join -->
  <section class="abs join">
   <h2>Join our "<b>Insider Advisory</b>" for <b>FREE.</b></h2>
   <p class="lead"><b>You'll receive</b> the latest research secrets while learning how to use psychology for gaining a decisive advantage to market and sell your wedding cakes.ur Name and Email Address Below.</p>
   <div class="joinbar">
    <span class="in">Your First Name</span>
    <span class="in">Your E-mail</span>
    <span class="btn">CLICK TO JOIN</span>
   </div>
   <p class="note"><b>We dislike spam as much as you do.</b> Therefore, we'll never sell, rent, or give away your email address.</p>
  </section>

  <!-- footer -->
  <footer class="abs footer">
   <div class="f-brand"><span class="dot"></span>Northfield Pastry</div>
   <div class="socials"><span></span><span></span><span></span></div>
   <div class="blog">
    <h4>Recent Blog Posts</h4>
    <div class="post"><span class="date">06-11-19</span>World's Greatest Wedding Cakes Bakers<span class="btn rm">Read More</span></div>
    <div class="post"><span class="date">10-11-19</span>Wedding CAMP Tour 2020<span class="btn rm">Read More</span></div>
    <p class="older">Read Older Posts &rarr;</p>
   </div>
   <div class="col" style="left:155px">
    <h5>Marketing Solutions</h5>
    <a>Cracking the Secret Code Course</a><a>Individual Marketing Videos</a><a>Bundled Marketing Videos</a><a>Gold Standard Baker</a><a>Advertise For Free</a><a>Analyze Your Marketing</a><a>Master Hierarchy Training</a>
   </div>
   <div class="col" style="left:400px">
    <h5>Sales Solutions</h5>
    <a>Individual Sales Tools</a><a>Bundles Sales Presentations</a><a>Advanced Insider Bulletin</a><a>Write a Wedding Cake Book</a><a>Analyze Your Sales System</a>
   </div>
   <div class="col" style="left:610px">
    <h5>Hire Us</h5>
    <a>Coaching Consulting</a><a>Speaking</a><a>3-Day Workshops</a>
    <h5 style="margin-top:22px">Partner With Us</h5>
    <a>Spread the Word</a>
   </div>
   <p class="copyright">© 2019 Northfield Pastry Ltd. All Right reserved.</p>
  </footer>

 </div>
</div>
</body>
</html>
```